VELMARKS COFFEE CUPS

I WANT A DESIGN FOR TAKE AWAY COFFEE CUPS 12 oz. IN THE ATTACHED PROFILES YOU'LL FIND THE LOGO AND SOME DESIGNS I LIKE (WHICH IS FLOWER OR COFFEE QOUTES) THE COLORS ARE PREFERLY WHITE, PINK, PURPLE OR YOU CAN DO OTHER COLORS IF NICER.

```html
<!DOCTYPE html>
<html lang="en">
<head>
<meta charset="utf-8">
<title>Velmarks Coffee Cups</title>
<link rel="stylesheet" href="https://fonts.googleapis.com/css2?family=Bebas+Neue&display=swap">
<style>
  :root {
    --page: #ffffff;
    --frame: #555555;
    --kraft: #d4aa78;
    --cup-edge: #5a4a3a;
    --ink: #111111;
    --brand: #333333;
    --lipstick: #e0191e;
  }
  html, body {
    margin: 0;
    padding: 0;
    overflow: hidden;
    background: var(--page);
  }
  .canvas {
    display: block;
    width: 1200px;
    height: 893px;
  }
  .canvas-frame { fill: var(--page); stroke: var(--frame); stroke-width: 1.5; }
  .cup-sleeve { fill: var(--kraft); stroke: var(--cup-edge); stroke-width: 1; }
  .brand-name, .brand-sub, .cup-quote {
    font-family: "Bebas Neue", "Arial Narrow", sans-serif;
    font-weight: 400;
    text-anchor: middle;
  }
  .brand-name, .brand-sub { fill: var(--brand); }
  .brand-name { letter-spacing: 2px; }
  .brand-sub { letter-spacing: 6px; }
  .cup-quote { fill: var(--ink); font-size: 67px; }
  .kiss-mark { fill: var(--lipstick); }
</style>
</head>
<body>
<svg class="canvas" viewBox="0 0 1200 893" xmlns="http://www.w3.org/2000/svg">
  <rect class="canvas-frame" x="1" y="1" width="1198" height="891"/>

  <g class="cup cup-rain">
    <polygon class="cup-sleeve" points="72,90 562,90 454,798 180,798"/>
    <text class="brand-name" x="317" y="268" font-size="92">VELMARKS</text>
    <text class="brand-sub" x="317" y="308" font-size="34">COFFEE</text>
    <text class="cup-quote" x="318" y="407">LET</text>
    <text class="cup-quote" x="318" y="485">THE</text>
    <text class="cup-quote" x="318" y="569">RAIN</text>
    <text class="cup-quote" x="318" y="645">KISS</text>
    <text class="cup-quote" x="318" y="725">YOU</text>
  </g>

  <g class="cup cup-kiss">
    <polygon class="cup-sleeve" points="625,90 1114,90 1006,798 732,798"/>
    <text class="brand-name" x="869" y="208" font-size="74">VELMARKS</text>
    <text class="brand-sub" x="869" y="240" font-size="28">COFFEE</text>
    <ellipse class="kiss-mark" cx="873" cy="328" rx="75" ry="52" role="img" aria-label="Red lipstick kiss print"/>
    <text class="cup-quote" x="869" y="445">A</text>
    <text class="cup-quote" x="869" y="525">SIP</text>
    <text class="cup-quote" x="869" y="601">OF</text>
    <text class="cup-quote" x="869" y="677">CLOSE</text>
    <text class="cup-quote" x="869" y="751">KISS</text>
  </g>
</svg>
</body>
</html>
```